Modern Billboard Ad for Criminal Defense Firm

10.5 x 36 We're looking for something to set us apart from the local competition. Looking for sleek and modern. We're a mid-sized firm in a small market city. We want to give the artist room to be creative on this one.
Thanks

Target Market(s)

Adult clients who have been charged with a crime/DWI

Industry/Entity Type

legal

Font styles to use
Serif
Sans Serif

Requirements
Must have
• Needs to have the firm name in large lettering. Law Offices of Marcus T Whitfield. “PLLC” does not have to be included. Phone number of (555) 384-1927 should be included but not the main focus.
Nice to have
• A call to action or something similar. “Don’t go it alone, call today.”, “ Arrested?”

```html
<!DOCTYPE html>
<html lang="en">
<head>
<meta charset="utf-8">
<title>Law Offices of Marcus T Whitfield — Billboard</title>
<link href="https://fonts.googleapis.com/css2?family=Cinzel:wght@500;700&family=Montserrat:wght@800&family=Arimo:wght@700&display=swap" rel="stylesheet">
<style>
  :root {
    --navy: #13254a;
    --white: #ffffff;
    --stage-blue: #3f5fab;
    --photo-light: #c9c9c9;
    --photo-dark: #3a3a3a;
  }
  html, body {
    margin: 0;
    padding: 0;
    width: 1200px;
    height: 1200px;
    overflow: hidden;
    background: var(--white);
  }
  .canvas {
    position: relative;
    width: 1200px;
    height: 1200px;
  }
  .stage-band {
    position: absolute;
    left: 0;
    top: 491px;
    width: 1200px;
    height: 709px;
    background: var(--stage-blue);
  }
  .billboard {
    position: absolute;
    width: 1071px;
    height: 318px;
    background: var(--navy);
    transform-origin: top left;
  }
  .billboard--light { left: 64px; top: 96px; }
  .billboard--dark { left: 116px; top: 669px; transform: scale(0.9); }

  .portrait {
    position: absolute;
    left: 9px;
    top: 9px;
    width: 305px;
    height: 300px;
    background: radial-gradient(ellipse at 55% 40%, var(--photo-light) 0%, #8a8a8a 45%, var(--photo-dark) 100%);
  }
  .name-panel {
    position: absolute;
    left: 314px;
    top: 9px;
    width: 748px;
    height: 181px;
    background: var(--white);
  }
  .rule {
    position: absolute;
    left: 396px;
    width: 612px;
    height: 2px;
    background: var(--navy);
  }
  .rule--top { top: 88px; }
  .rule--bottom { top: 172px; }
  .firm-kicker {
    position: absolute;
    left: 396px;
    width: 612px;
    top: 32px;
    margin: 0;
    text-align: center;
    font-family: "Cinzel", serif;
    font-weight: 500;
    font-size: 46px;
    line-height: 1;
    color: var(--navy);
    letter-spacing: 1px;
  }
  .firm-name {
    position: absolute;
    left: 386px;
    width: 632px;
    top: 106px;
    margin: 0;
    text-align: center;
    font-family: "Cinzel", serif;
    font-weight: 700;
    font-size: 57px;
    line-height: 60px;
    color: var(--navy);
    white-space: nowrap;
  }
  .cta {
    position: absolute;
    left: 380px;
    width: 660px;
    top: 204px;
    margin: 0;
    text-align: center;
    font-family: "Montserrat", sans-serif;
    font-weight: 800;
    font-size: 26px;
    letter-spacing: 1.8px;
    color: var(--white);
    text-transform: uppercase;
    white-space: nowrap;
  }
  .phone {
    position: absolute;
    left: 400px;
    width: 620px;
    top: 246px;
    margin: 0;
    text-align: center;
    font-family: "Arimo", sans-serif;
    font-weight: 700;
    font-size: 38px;
    letter-spacing: 1.6px;
    color: var(--white);
  }
  .award-seal {
    position: absolute;
    left: 231px;
    top: 151px;
    width: 156px;
    height: 156px;
  }
</style>
</head>
<body>
<div class="canvas">
  <div class="stage-band"></div>

  <section class="billboard billboard--light">
    <div class="portrait" role="img" aria-label="Black and white portrait of the attorney in a vest and tie, jacket over shoulder, against a wood wall"></div>
    <div class="name-panel"></div>
    <p class="firm-kicker">Law Offices of</p>
    <div class="rule rule--top"></div>
    <h1 class="firm-name">Marcus T Whitfield</h1>
    <div class="rule rule--bottom"></div>
    <svg class="award-seal" viewBox="0 0 156 156" role="img" aria-label="Community award seal">
      <circle cx="78" cy="78" r="78" fill="#ffffff"/>
      <circle cx="78" cy="78" r="70" fill="#13254a"/>
    </svg>
    <p class="cta">Don’t go it alone, call today.....</p>
    <p class="phone">(555) 384-1927</p>
  </section>

  <section class="billboard billboard--dark">
    <div class="portrait" role="img" aria-label="Black and white portrait of the attorney in a vest and tie, jacket over shoulder, against a wood wall"></div>
    <div class="name-panel"></div>
    <p class="firm-kicker">Law Offices of</p>
    <div class="rule rule--top"></div>
    <h2 class="firm-name">Marcus T Whitfield</h2>
    <div class="rule rule--bottom"></div>
    <svg class="award-seal" viewBox="0 0 156 156" role="img" aria-label="Community award seal">
      <circle cx="78" cy="78" r="78" fill="#ffffff"/>
      <circle cx="78" cy="78" r="70" fill="#13254a"/>
    </svg>
    <p class="cta">Don’t go it alone, call today.....</p>
    <p class="phone">(555) 384-1927</p>
  </section>
</div>
</body>
</html>
```